Wellness Thai Massage Geschäft benötigt eine Preis/Info Broschüre

Ein kleines Thai Massage Geschäft in Bayern: Sukonta Thaimassage
Benötigt eine kleine Preisliste, sowie eine kurze Beschreibung vom Unternehmen. Angeboten werden traditionelle Thaimassagen. Der Farbstil soll dem Logo (Anhang) angepasst sein. Alle Bilder außer die Bilder von der Geschäftsführerin sind optional zur Verwendung verfügbar. Mehr Info wie Preise, etc. sind verfügbar auf der Website https://www.sukontathaimassage-beispiel.de/

```html
<!DOCTYPE html>
<html lang="de">
<head>
<meta charset="utf-8">
<title>Sukonta Thaimassage – Preis- und Infobroschüre</title>
<link href="https://fonts.googleapis.com/css2?family=Montserrat:ital,wght@0,400;0,500;0,600;1,400&display=swap" rel="stylesheet">
<style>
  :root {
    --wine: #8c1a2d;
    --wine-deep: #741322;
    --wine-light: #a5304a;
    --blush: #f2cdd2;
    --rose: #e3a0ab;
    --rose-dark: #c9707f;
    --gold: #f4b43a;
    --cream: #fbeec6;
    --white: #ffffff;
    --ink-wine: #7a1526;
    --canvas: #ece7e4;
  }
  * { margin: 0; padding: 0; box-sizing: border-box; }
  html, body { width: 1200px; height: 900px; overflow: hidden; }
  body {
    background: var(--canvas);
    font-family: "Montserrat", Arial, sans-serif;
    position: relative;
  }
  .flyer {
    position: absolute;
    top: 54px;
    width: 560px;
    height: 792px;
    overflow: hidden;
    background: linear-gradient(180deg, var(--wine-light) 0%, var(--wine) 55%, var(--wine-deep) 100%);
    box-shadow: 0 6px 24px rgba(60, 20, 25, 0.25);
  }
  .flyer--about { left: 25px; }
  .flyer--prices { left: 615px; }

  .layer { position: absolute; inset: 0; width: 560px; height: 792px; }

  .photo {
    position: absolute;
    background: linear-gradient(135deg, #d9b27a 0%, #b0674f 45%, #6e2a2a 100%);
  }
  .photo--massage { left: 0; top: 0; width: 560px; height: 350px; }
  .photo--therapist {
    left: 300px; top: 0; width: 260px; height: 260px;
    background: linear-gradient(160deg, #c98a6c 0%, #b94a4a 50%, #7b1e2a 100%);
  }

  .round-photo {
    position: absolute;
    border-radius: 50%;
    border: 5px solid var(--blush);
    background: radial-gradient(circle at 40% 35%, #c89a72 0%, #6d3b30 60%, #3a1c1a 100%);
  }

  .decor-bloom {
    position: absolute;
    border-radius: 50%;
    background: radial-gradient(circle, rgba(230, 130, 150, 0.22) 0%, rgba(230, 130, 150, 0) 70%);
  }

  .brand {
    position: absolute;
    left: 18px;
    top: 26px;
    display: flex;
    align-items: center;
    gap: 12px;
  }
  .brand__mark {
    width: 54px; height: 46px;
    background: var(--cream);
  }
  .brand__name {
    color: var(--gold);
    font-weight: 600;
    font-size: 15px;
    line-height: 1.25;
    letter-spacing: 1.5px;
    text-transform: uppercase;
  }

  .headline {
    position: absolute;
    color: var(--white);
    font-weight: 400;
    font-size: 22px;
    line-height: 1.25;
  }

  .section-title {
    color: var(--gold);
    font-weight: 400;
    font-size: 21px;
    margin-bottom: 8px;
  }
  .body-copy {
    color: var(--white);
    font-size: 10.5px;
    line-height: 1.45;
    text-align: justify;
  }
  .about-text {
    position: absolute;
    left: 40px;
    width: 470px;
  }

  .note {
    position: absolute;
    color: rgba(255, 255, 255, 0.85);
    font-style: italic;
    font-size: 9px;
    line-height: 1.45;
  }

  .contact {
    position: absolute;
    right: 22px;
    bottom: 20px;
    text-align: right;
    color: var(--ink-wine);
  }
  .contact__name { font-size: 17px; font-weight: 400; margin-bottom: 4px; }
  .contact__web { font-size: 10px; margin-bottom: 5px; }
  .contact__line {
    font-size: 7.5px;
    line-height: 1.5;
    display: flex;
    justify-content: flex-end;
    align-items: center;
    gap: 4px;
  }
  .contact__line svg { width: 8px; height: 8px; }

  .services {
    position: absolute;
    top: 300px;
    display: flex;
    flex-direction: column;
    gap: 18px;
  }
  .services--left { left: 36px; width: 258px; }
  .services--right { left: 318px; width: 212px; top: 268px; }

  .service__title {
    display: flex;
    align-items: center;
    gap: 7px;
    color: var(--gold);
    font-size: 13px;
    font-weight: 400;
    line-height: 1.15;
    margin-bottom: 5px;
  }
  .service__dot {
    flex: none;
    width: 14px; height: 14px;
    border-radius: 50%;
    background: var(--rose);
  }
  .service__text {
    color: var(--white);
    font-size: 9px;
    line-height: 1.38;
    text-align: justify;
  }
  .service__prices {
    margin-top: 9px;
    color: var(--rose);
    font-size: 9px;
    font-weight: 600;
    line-height: 1.45;
  }
</style>
</head>
<body>

<!-- Seite 1: Info über Thai Massage und das Studio -->
<section class="flyer flyer--about">
  <div class="photo photo--massage" role="img" aria-label="Foto: Therapeutin bei einer traditionellen Thai-Massage im Studio"></div>

  <svg class="layer" viewBox="0 0 560 792" aria-hidden="true">
    <path d="M0 0 H310 C270 70 170 110 0 130 Z" fill="var(--wine)"/>
    <path d="M0 330 C160 300 300 390 560 300 V350 C330 430 160 360 0 400 Z" fill="var(--blush)"/>
    <path d="M0 400 C160 360 330 430 560 350 V792 H0 Z" fill="var(--wine)"/>
    <path d="M0 400 C160 360 330 430 560 350" fill="none" stroke="var(--rose)" stroke-width="3"/>
    <path d="M560 600 C440 640 330 710 300 792 H560 Z" fill="var(--rose)"/>
    <path d="M560 630 C455 665 365 720 340 792 H560 Z" fill="var(--blush)" opacity="0.55"/>
  </svg>

  <div class="decor-bloom" style="left:330px; top:430px; width:230px; height:230px;" role="img" aria-label="Zarte Orchideen als Hintergrunddekoration"></div>

  <div class="round-photo" style="left:40px; top:245px; width:150px; height:150px;" role="img" aria-label="Foto: Buddha-Statue mit Blüten"></div>
  <div class="round-photo" style="left:165px; top:262px; width:140px; height:140px;" role="img" aria-label="Foto: Hot Stones und Massageöle"></div>

  <div class="brand">
    <div class="brand__mark"></div>
    <div class="brand__name">Sukonta<br>Thaimassage</div>
  </div>

  <div class="about-text" style="top:425px;">
    <h2 class="section-title">Was ist Thai Massage eigentlich?</h2>
    <p class="body-copy">Thai Massage existiert schon seit ca. über 2500 Jahren welches sich im Laufe der Zeit zu einer effektiven Methode gegen Schmerzzustände und auch Krankheiten entwickelt welches in der heutigen Zeit sogar Kultstatus erreicht hat. Diese thailändische Heilungsmethode verlangt eine professionelle Ausbildung die Hintergrundwissen und langes Training mit sich bringt.</p>
  </div>

  <div class="about-text" style="top:560px; width:420px;">
    <h2 class="section-title">Über uns</h2>
    <p class="body-copy">Sukonta Thaimassage legt einen hohen Wert auf die Zufriedenheit und das Wohlbefinden von jedem Kunden. Wenn sie also z.B nach viel Arbeit gestresst sind und Schmerzen an einer bestimmten Region aufgebaut haben, dann sind sie bei uns an der richtigen Adresse. Geführt wird das Massagestudio von Malee Sommer, die professionell ausgebildet wurde und auch beruflich schon in Deutschland sowie in Thailand viel Erfahrung gesammelt hat. Wir freuen uns schon auf ihren Besuch bei Sukonta Thaimassage!</p>
  </div>

  <p class="note" style="left:40px; top:748px;">Bitte erkundigen sie sich hierfür im Geschäft um<br>über ein erweitertes Angebot zu erfahren.</p>

  <div class="contact">
    <p class="contact__name">Sukonta Thaimassage</p>
    <p class="contact__web">www.sukontathaimassage-beispiel.de</p>
    <p class="contact__line">
      <svg viewBox="0 0 10 10"><path d="M2 1 L4 3 L3 4 Q4 6 6 7 L7 6 L9 8 L8 9 Q3 9 1 2 Z" fill="var(--ink-wine)"/></svg>0170 4418823
      <svg viewBox="0 0 10 10"><rect x="1" y="2" width="8" height="6" fill="none" stroke="var(--ink-wine)"/><path d="M1 2 L5 5 L9 2" fill="none" stroke="var(--ink-wine)"/></svg>info@sukonta-beispiel.de
    </p>
    <p class="contact__line">Lindenweg 14, 83022 Rosenheim, Deutschland</p>
  </div>
</section>

<!-- Seite 2: Angebot und Preise -->
<section class="flyer flyer--prices">
  <div class="photo photo--therapist" role="img" aria-label="Foto: Therapeutin bei einer Dehnübung im Behandlungsraum"></div>

  <svg class="layer" viewBox="0 0 560 792" aria-hidden="true">
    <path d="M0 0 H300 C320 80 320 170 300 260 C200 240 90 210 0 225 Z" fill="var(--wine)"/>
    <path d="M0 225 C140 205 300 290 560 225 V270 C330 330 150 265 0 290 Z" fill="var(--blush)"/>
    <path d="M0 290 C150 265 330 330 560 270 V792 H0 Z" fill="var(--wine)"/>
    <path d="M0 290 C150 265 330 330 560 270" fill="none" stroke="var(--rose)" stroke-width="3"/>
    <path d="M560 585 C450 620 370 700 345 792 H560 Z" fill="var(--rose)"/>
    <path d="M560 615 C465 650 395 715 380 792 H560 Z" fill="var(--blush)" opacity="0.55"/>
  </svg>

  <div class="decor-bloom" style="left:330px; top:420px; width:220px; height:220px;" role="img" aria-label="Zarte Orchideen als Hintergrunddekoration"></div>

  <div class="brand">
    <div class="brand__mark"></div>
    <div class="brand__name">Sukonta<br>Thaimassage</div>
  </div>

  <h1 class="headline" style="left:30px; top:100px;">Thailändische<br>Heilungsmethode verlangt</h1>

  <div class="round-photo" style="left:28px; top:178px; width:100px; height:100px;" role="img" aria-label="Foto: Hot Stones und Massageöle"></div>
  <div class="round-photo" style="left:112px; top:182px; width:100px; height:100px;" role="img" aria-label="Foto: Behandlungsraum mit Massageliege"></div>
  <div class="round-photo" style="left:196px; top:178px; width:100px; height:100px;" role="img" aria-label="Foto: Massageöle und Tiegel"></div>

  <div class="services services--left">
    <article class="service">
      <h3 class="service__title"><span class="service__dot"></span>Traditionelle<br>Thai-Sport Massage</h3>
      <p class="service__text">Mit der traditionellen Thai-Massage werden durch Akupressur, Dehnung und Energielinien-Massage Energieblockaden gelöst. Es wird an 10 Energiepunkten und Linien massiert, die für den Einklang von Körper und Geist wichtig sind. Somit wird eine innere Balance und der Fluss der Lebensenergie erreicht</p>
      <p class="service__prices">60 Minuten = 54 Euro<br>90 Minuten = 76 Euro</p>
    </article>
    <article class="service">
      <h3 class="service__title"><span class="service__dot"></span>Aromaöl Massage</h3>
      <p class="service__text">Die Aromaöl Massage ist eine Behandlungsform zur Regeneration und Harmonisierung des gesamten Körpers. Dabei wird das Basisöl mit ätherischen Ölen angereichert. Die Aromatherapie kann anregend oder entspannend abgestimmt werden</p>
      <p class="service__prices">60 Minuten = 51 Euro<br>90 Minuten = 72 Euro</p>
    </article>
    <article class="service">
      <h3 class="service__title"><span class="service__dot"></span>Hot Stone Massage</h3>
      <p class="service__text">Bei der Hot Stone Massage werden angewärmte Vulkansteine entlang der Energielinien angebracht. Durch die abgegebene gespeicherte Wärme wird der Energiefluss und die Blutzirkulation gesteigert. Es kommt im ganzen Körper zu einer Tiefenentspannung</p>
      <p class="service__prices">90 Minuten = 83 Euro</p>
    </article>
  </div>

  <div class="services services--right">
    <article class="service">
      <h3 class="service__title"><span class="service__dot"></span>Fussreflexzonen<br>Massage</h3>
      <p class="service__text">Eine Massage für den wohl für den strapaziertesten Körperteil, den Füssen, setzt neue Kräfte frei und verleiht Vitalität</p>
      <p class="service__prices">30 Minuten = 35 Euro<br>60 Minuten = 62 Euro</p>
    </article>
    <article class="service">
      <h3 class="service__title"><span class="service__dot"></span>Rücken-Thai Massage</h3>
      <p class="service__text">Bei dieser Massagetechnik wird größtenteils der Rücken sowie auch Nacken, Hinterkopf, Schulter und Finger involviert. Diese Massage eignet sich besonders falls eines dieser Bereiche verspannt oder Schmerzen verursacht.</p>
      <p class="service__prices">30 Minuten = 35 Euro<br>60 Minuten = 72 Euro</p>
    </article>
    <p class="note" style="position:static; margin-top:4px;">Bitte erkundigen sie sich hierfür im Geschäft um über ein erweitertes Angebot zu erfahren.</p>
  </div>

  <div class="contact">
    <p class="contact__name">Sukonta Thaimassage</p>
    <p class="contact__web">www.sukontathaimassage-beispiel.de</p>
    <p class="contact__line">
      <svg viewBox="0 0 10 10"><path d="M2 1 L4 3 L3 4 Q4 6 6 7 L7 6 L9 8 L8 9 Q3 9 1 2 Z" fill="var(--ink-wine)"/></svg>0170 4418823
      <svg viewBox="0 0 10 10"><rect x="1" y="2" width="8" height="6" fill="none" stroke="var(--ink-wine)"/><path d="M1 2 L5 5 L9 2" fill="none" stroke="var(--ink-wine)"/></svg>info@sukonta-beispiel.de
    </p>
    <p class="contact__line">Lindenweg 14, 83022 Rosenheim, Deutschland</p>
  </div>
</section>

</body>
</html>
```